Letterhead Design Project For Australian Accounting Firm

Hi All,

We need a letterhead designed for our Australian Accounting firm based in Melbourne, Victoria. I have already got a logo and business cards designed which i will add to this brief. Please design the letterhead with reference to the logo and business cards, all three items need to match. The following information needs to be included on the letterhead:

KM Associates Logo

Suite 4 527 Harlow Street, Brunswick VIC 3056
PO Box 748, Brunswick VIC 3056

Lena Vardakis B.Com FQ
Director
0491 634 207

Barnaby Whitlock B.Bus FQ
Director
0433 580 716

www.kmassociates.com.au

at the bottom of the letterhead in small size font there needs to be the following phrase:

Liability limited by a scheme approved under Professional Standards Legislation.

Also please try and incorporate the FQ logo somewhere on the letterhead

We are looking for a sharp and modern looking letterhead design, something that incorporates the look of the business card and logo.

Thanks.

```html
<!DOCTYPE html>
<html lang="en">
<head>
<meta charset="utf-8">
<title>KM Associates Letterhead</title>
<link href="https://fonts.googleapis.com/css2?family=Source+Sans+3:wght@400;600&display=swap" rel="stylesheet">
<style>
  :root {
    --ink: #111111;
    --paper: #ffffff;
    --accent: #d9232e;
    --rule: #444444;
  }
  * { margin: 0; padding: 0; box-sizing: border-box; }
  html, body { width: 849px; height: 1200px; overflow: hidden; background: var(--paper); }
  body { font-family: "Source Sans 3", Arial, sans-serif; color: var(--ink); }
  .letterhead { position: relative; width: 849px; height: 1200px; }

  .brand-block {
    position: absolute; left: 0; top: 0; width: 420px; height: 170px;
    background: var(--ink); color: var(--paper);
  }
  .brand-name {
    position: absolute; left: 28px; top: 66px;
    font-size: 20px; font-weight: 600; letter-spacing: 0.5px; white-space: nowrap;
  }
  .brand-divider {
    position: absolute; left: 176px; top: 42px; width: 2px; height: 118px; background: var(--paper);
  }
  .brand-services {
    position: absolute; left: 195px; top: 74px;
    font-size: 26px; font-weight: 400; line-height: 28px; letter-spacing: 0.2px;
  }

  .address {
    position: absolute; right: 19px; top: 44px; text-align: right;
    font-size: 16.5px; line-height: 21px;
  }

  .director { position: absolute; top: 122px; font-size: 16px; line-height: 22px; }
  .director-left { left: 438px; }
  .director-right { right: 19px; text-align: right; }
  .director-name { font-weight: 600; }
  .director-phone { display: flex; align-items: center; gap: 14px; margin-top: 1px; }
  .director-right .director-phone { justify-content: flex-end; gap: 22px; }
  .phone-icon { width: 11px; height: 13px; display: block; }
  .director-divider {
    position: absolute; left: 636px; top: 124px; width: 1px; height: 60px; background: var(--rule);
  }

  .badge { position: absolute; left: 24px; top: 1122px; width: 52px; height: 52px; }
  .website {
    position: absolute; right: 42px; top: 1108px; font-size: 17px; letter-spacing: 0.3px;
  }
  .liability-band {
    position: absolute; left: 213px; top: 1134px; width: 636px; height: 30px;
    background: var(--ink); color: var(--paper);
    font-size: 16px; line-height: 30px; text-align: center; padding-left: 14px;
  }
</style>
</head>
<body>
<div class="letterhead">
  <header>
    <div class="brand-block">
      <div class="brand-name">KM Associates</div>
      <div class="brand-divider"></div>
      <div class="brand-services">TAXATION AND<br>BUSINESS SERVICES</div>
    </div>

    <div class="address">
      <p>Suite 4 527 Harlow Street, Brunswick VIC 3056</p>
      <p>PO Box 748, Brunswick VIC 3056</p>
    </div>

    <div class="director director-left">
      <p class="director-name">Lena Vardakis B.Com FQ</p>
      <p>Director</p>
      <p class="director-phone">
        <svg class="phone-icon" viewBox="0 0 11 13" aria-hidden="true"><rect x="0" y="0" width="11" height="13" rx="1.5" fill="#111"/><rect x="2" y="2" width="7" height="5" fill="#fff"/></svg>
        <span>0491 634 207</span>
      </p>
    </div>
    <div class="director-divider"></div>
    <div class="director director-right">
      <p class="director-name">Barnaby Whitlock B.Bus FQ</p>
      <p>Director</p>
      <p class="director-phone">
        <svg class="phone-icon" viewBox="0 0 11 13" aria-hidden="true"><rect x="0" y="0" width="11" height="13" rx="1.5" fill="#111"/><rect x="2" y="2" width="7" height="5" fill="#fff"/></svg>
        <span>0433 580 716</span>
      </p>
    </div>
  </header>

  <footer>
    <svg class="badge" viewBox="0 0 52 52" role="img" aria-label="Professional membership badge">
      <circle cx="26" cy="26" r="25" fill="var(--accent)"/>
    </svg>
    <p class="website">www.kmassociates.com.au</p>
    <p class="liability-band">Liability limited by a scheme approved under Professional Standards Legislation.</p>
  </footer>
</div>
</body>
</html>
```